Geschäftspapiere für Termin Startup
Zielgruppe
Wir sind ein Startup, das über die Seite Planorix.de (derzeit noch in der Beta-Phase)zukünftig folgenden Service anbietet: Unternehmer können sehr flexibel (selbst) gestaltete Terminformulare erstellen und auf Ihrer Website einbinden. Kunden können dann diese Termine buchen und bekommen dann Erinnerungs-Mails und SMS.
Zielgruppe: Dienstleister wie Fotografen, Friseure, Versicherungsvertreter, Masseure, Restaurants, Arztpraxen. Also alle, die darauf angewiesen sind, dass vereinbarte Termine eingehalten werden und die die Terminvereinbarung vereinfachen wollen. Also weniger per Telefon, mehr über die eigene Website.
Dateien bitte beachten für die Ansicht des Look & Feels:
https://ablage.beispielwolke.de/open?id=7QmrtHkWz2LpA94bNc3sVyTeOx8dGJuR_
Bonus-Aktion: Wir zahlen pauschal jeweils 30,00 Euro an die Designer auf den Plätzen 2 bis 4 für die geleistete Arbeit. Nur einer kann gewinnen und den Zuschlag bekommen. Aber so möchten wir gerne die Arbeit dennoch honorieren.
Aufgabenstellung
Wir benötigen ein modernes Briefpapier-Layout passend zu unserem CD.
Gerne darf/soll der ORBO (siehe Maskottchen in https://ablage.beispielwolke.de/open?id=5PwqNsYt8BaLmr2Hc7xkDuQOEPfjWzVbn )darauf erscheinen.
Maskottchen ORBO gibt es in mehreren Varianten. Siehe https://ablage.beispielwolke.de/ordner/8TrnWqLeHd5XcmZ3sJ4yPvBkGfQaNuRox?teilen=ja
Auch als Variante, das Maskottchen ORBO gegen das Logo gelehnt ist, kann genutzt werden: https://ablage.beispielwolke.de/open?id=3MuxBgTpW7RkaNj6yVqLeDsHcZoPfGtYi
Das Thema 'Terminvereinbarung' soll sofort erfasst werden mittels des Layouts bzw. der grafischen Elemente.
Auch die Branchen-Icons ( https://ablage.beispielwolke.de/ordner/6HpvRtNmQ2WkzLx8yEcBaJdFsUoGiTbeq?teilen=ja ) dürfen verwendet werden.

```html
<!DOCTYPE html>
<html lang="de">
<head>
<meta charset="utf-8">
<title>Planorix Briefpapier</title>
<link href="https://fonts.googleapis.com/css2?family=Open+Sans:wght@400;600;700&display=swap" rel="stylesheet">
<style>
:root{
  --green:#8cc63f;
  --grey:#6d7a80;
  --ink:#3c4043;
  --muted:#8a9094;
  --paper:#ffffff;
  --backdrop:#d9d9d9;
}
*{margin:0;padding:0;box-sizing:border-box}
html,body{width:1200px;height:968px;overflow:hidden;background:var(--backdrop);font-family:"Open Sans",Arial,sans-serif;color:var(--ink)}
.letterhead{position:absolute;left:282px;top:34px;width:636px;height:900px;background:var(--paper);box-shadow:0 2px 10px rgba(0,0,0,.15);overflow:hidden}
.top-rule{position:absolute;left:0;top:0;width:100%;height:4px;background:var(--green)}
.brand{position:absolute;right:40px;top:44px;text-align:right}
.brand-row{display:flex;align-items:center;gap:10px;justify-content:flex-end}
.brand-mark{width:22px;height:22px;background:var(--green)}
.brand-name{font-size:38px;font-weight:700;color:var(--green);line-height:1}
.brand-tagline{font-size:10px;color:var(--muted);margin-top:2px}
.sender-line{position:absolute;left:60px;top:128px;font-size:6px;color:var(--ink);border-bottom:.8px solid var(--ink);padding-bottom:2px;width:200px}
.fold-mark{position:absolute;left:0;width:18px;height:0;border-top:.8px solid #bbb}
.fold-top{top:300px}.fold-bottom{top:600px}
.contact{position:absolute;left:468px;top:200px;border-left:.8px solid var(--ink);padding-left:12px;font-size:8.5px;line-height:1.6;font-style:normal}
.contact-item{display:flex;align-items:center;gap:5px}
.contact-item svg{width:8px;height:8px;fill:var(--green)}
.recipient{position:absolute;left:60px;top:190px;font-size:9px}
.body-copy{position:absolute;left:60px;top:218px;width:380px;font-size:8.4px;line-height:1.55}
.body-copy p{margin-bottom:8px}
.signature{position:absolute;left:60px;top:470px;width:130px;height:34px;background:linear-gradient(90deg,#e6e6e6,#f3f3f3);border-radius:2px}
.footer-info{position:absolute;top:760px;left:0;width:100%;display:flex;font-size:8px;line-height:1.5;padding-left:60px}
.footer-col{padding:0 16px;border-left:.8px solid var(--ink)}
.footer-col:first-child{border-left:none;padding-left:0}
.footer-band{position:absolute;left:0;bottom:0;width:100%;height:70px;background:var(--green);border-top:8px solid var(--grey)}
.web-url{position:absolute;left:60px;bottom:30px;font-size:10px;color:#fff}
.mascot{position:absolute;left:490px;top:740px;width:60px;height:70px;background:radial-gradient(circle at 50% 45%,#a9d36e,#7b8a8f);border-radius:10px}
</style>
</head>
<body>
<main class="letterhead">
  <div class="top-rule"></div>

  <header class="brand">
    <div class="brand-row">
      <span class="brand-mark"></span>
      <span class="brand-name">Planorix</span>
    </div>
    <div class="brand-tagline">Tool by termin-werk.com</div>
  </header>

  <div class="sender-line">Planorix | Lindenallee 24 | 88410 Beispielstadt</div>
  <span class="fold-mark fold-top"></span>
  <span class="fold-mark fold-bottom"></span>

  <address class="contact">
    <div>Lindenallee 24</div>
    <div>88410 Beispielstadt</div>
    <div class="contact-item"><svg viewBox="0 0 10 10"><path d="M2 0h2l1 3-1.5 1a6 6 0 0 0 2.5 2.5L7 5l3 1v2a2 2 0 0 1-2 2A8 8 0 0 1 0 2a2 2 0 0 1 2-2z"/></svg>+49 (0) 7355 - 210</div>
    <div class="contact-item"><svg viewBox="0 0 10 10"><rect x="1" y="2" width="8" height="7"/><rect x="2" y="0" width="6" height="2"/></svg>+49 (0) 7355 - 210</div>
    <div class="contact-item"><svg viewBox="0 0 10 10"><path d="M0 2h10v6H0z"/></svg>info@planorix.de</div>
  </address>

  <div class="recipient">Herr Lindner</div>
  <section class="body-copy">
    <p>Lorem ipsum dolor sit amet, consectetur adipiscing elit. Proin tincidunt, lectus id malesuada cursus, lorem augue egestas magna, ut mattis orci ante ut arcu. Sed mauris tellus, fermentum quis ligula nec, posuere pulvinar eros. Nam at mi quis velit pellentesque finibus. Donec lacus velit, faucibus mollis dolor nec, finibus pellentesque orci. Duis sed dictum elit, ut posuere arcu. Phasellus ac dolor et ante consequat rutrum nec nec tortor. Donec consequat, nibh sit amet pulvinar faucibus, turpis magna venenatis diam, vel pretium eros erat vestibulum nulla.</p>
    <p>Sed pretium ac enim eu viverra. Aliquam ac est eget magna convallis convallis. Aenean augue purus, finibus eget turpis quis, finibus dignissim nibh. Phasellus viverra lobortis dignissim. Duis varius turpis in sapien accumsan facilisis. Sed vehicula gravida diam a interdum. Nullam convallis ligula id erat egestas consequat. Integer consectetur ex vel aliquet iaculis. Vestibulum molestie sodales mauris, at tincidunt risus pellentesqu.</p>
    <p>Mauris facilisis, lectus at accumsan tincidunt, dui magna imperdiet sem, quis tempor est lectus eu ipsum. Praesent in fermentum nisl. Maecenas at lorem at odio interdum iaculis. Pellentesque cursus nulla nunc, ut suscipit nulla maximus et. Donec maximus rhoncus metus, vel laoreet nisi pretium sit amet. Donec posuere enim lectus, vitae aliquam augue tincidunt dignissim. Morbi vitae congue velit, quis elementum.</p>
  </section>
  <div class="signature" role="img" aria-label="Handschriftliche Unterschrift von Jonas Beispiel"></div>

  <footer class="footer-info">
    <div class="footer-col">Steuerliche ID: DE000000000<br>Umsatzsteuer ID: 00 000 000 000</div>
    <div class="footer-col">Bankverbindung:<br>Nordbank Berlin</div>
    <div class="footer-col">BIC: NORBDEFF000<br>IBAN: DE00 1234 5678 9012 3456 78</div>
  </footer>

  <div class="mascot" role="img" aria-label="Maskottchen mit Kalender, winkend"></div>

  <div class="footer-band" aria-hidden="true"></div>
  <div class="web-url">www.planorix.de</div>
</main>
</body>
</html>
```